Kugelhaus Sports- & Billardbar

Hello,
I Need a Chatterly-Design for my Sports- & Billardbar.
It should include a Profile Picture and a title Picture (Banner).
The following Information should be included in the banner:

"Official Logo (attached)

5 Pool-Billard Tische
3 Snooker Tische
3 Dart-Automaten
1 Tischkicker

1 Großbildleinwand
4 TV-Geräte
2 Orbo-Leitungen
Alle Sportevents LIVE & in HD

Kugelhaus, Fennweg 14, 72519 Reutlingen"

I have attached the Logo and some Pictures, which can be used, but don`t have to. You can just try them out. They are not best Quality though.
I have also attached the Logo of the Kronenliga, Vesper Cup, etc.
This Logos should get included!

The corporate Colors are the same than the official "Kugelhaus"-Logo.

If you have any questions, just contact me!

Thanks in Advance!

Tobias

```html
<!DOCTYPE html>
<html lang="de">
<head>
<meta charset="utf-8">
<title>Kugelhaus – Billard, Sportsbar, Lounge</title>
<link rel="stylesheet" href="https://fonts.googleapis.com/css2?family=Oswald:wght@500;700&display=swap">
<style>
  :root {
    --teal: #4fb8bb;
    --teal-soft: #9fd6cf;
    --ink: #3b3b3d;
    --ink-dark: #2e2e30;
    --paper: #ecebe8;
    --band: rgba(255,255,255,0.82);
    --badge: #d9d9d6;
    --badge-edge: #bdbdba;
  }
  * { margin: 0; padding: 0; box-sizing: border-box; }
  html, body { width: 1200px; height: 444px; overflow: hidden; background: var(--paper); }
  .banner {
    position: relative; width: 1200px; height: 444px; overflow: hidden;
    font-family: "Oswald", "Arial Narrow", sans-serif; text-transform: uppercase; color: var(--ink);
  }
  .backdrop { position: absolute; inset: 0; }
  .tagline-box {
    position: absolute; left: 0; top: 25px; width: 423px; height: 38px;
    background: var(--band); clip-path: polygon(0 0, 100% 0, 96% 100%, 0 100%);
  }
  .tagline-box span {
    position: absolute; left: 14px; top: 3px; font-size: 22px; font-weight: 500; letter-spacing: 1px;
  }
  .amenity {
    position: absolute; font-size: 20px; font-weight: 500; letter-spacing: 0.8px; white-space: nowrap;
  }
  .amenity b { font-weight: 500; margin-right: 12px; }
  .brand {
    position: absolute; right: 33px; top: 22px; text-align: right;
  }
  .brand-name {
    font-size: 86px; font-weight: 700; line-height: 1; color: var(--ink-dark); letter-spacing: 1px;
  }
  .brand-sub { font-size: 14px; font-weight: 500; letter-spacing: 1.4px; margin-top: 2px; }
  .badges { position: absolute; left: 0; top: 0; }
  .info-band {
    position: absolute; left: 606px; top: 290px; width: 494px; height: 64px;
    background: var(--band); clip-path: polygon(3% 0, 100% 0, 97% 100%, 0 100%);
    text-align: center;
  }
  .info-band .headline { color: var(--teal); font-size: 17px; font-weight: 500; letter-spacing: 0.8px; margin-top: 4px; }
  .info-band .address { color: var(--ink-dark); font-size: 22px; font-weight: 500; letter-spacing: 0.6px; line-height: 1.2; }
</style>
</head>
<body>
<main class="banner">
  <svg class="backdrop" width="1200" height="444" viewBox="0 0 1200 444" role="img" aria-label="Facettiertes Dreiecksmuster in Türkis, Mint und Hellgrau">
    <defs>
      <linearGradient id="tealField" x1="0" y1="0" x2="1" y2="1">
        <stop offset="0" stop-color="#7cc9c4"/>
        <stop offset="0.45" stop-color="#a9d8c9"/>
        <stop offset="0.75" stop-color="#d8d4b8"/>
        <stop offset="1" stop-color="#b7cfc5"/>
      </linearGradient>
      <linearGradient id="greyField" x1="0" y1="0" x2="1" y2="0">
        <stop offset="0" stop-color="#f2f1ee"/>
        <stop offset="1" stop-color="#dcdcda"/>
      </linearGradient>
      <linearGradient id="tealCorner" x1="1" y1="0" x2="0" y2="1">
        <stop offset="0" stop-color="#7ccac3"/>
        <stop offset="1" stop-color="#cfe3da" stop-opacity="0"/>
      </linearGradient>
    </defs>
    <rect width="1200" height="444" fill="url(#greyField)"/>
    <polygon points="0,0 700,0 520,444 0,444" fill="url(#tealField)"/>
    <polygon points="1080,250 1200,180 1200,444 1000,444" fill="url(#tealCorner)"/>
  </svg>

  <div class="tagline-box"><span>Billard - Sportsbar - Lounge</span></div>

  <p class="amenity" style="left:399px; top:80px;"><b>1</b>Großbildleinwand</p>
  <p class="amenity" style="left:124px; top:108px;"><b>5</b>Pool-Billard Tische</p>
  <p class="amenity" style="left:360px; top:135px;"><b>4</b>TV-Geräte</p>
  <p class="amenity" style="left:89px; top:164px;"><b>3</b>Snooker Tische</p>
  <p class="amenity" style="left:329px; top:190px;"><b>2</b>Orbo-Leitungen</p>
  <p class="amenity" style="left:59px; top:217px;"><b>3</b>Dart-Automaten</p>
  <p class="amenity" style="left:300px; top:246px;"><b>1</b>Tischkicker</p>

  <div class="brand">
    <div class="brand-name">Kugelhaus</div>
    <div class="brand-sub">Billard - Sportsbar - Lounge</div>
  </div>

  <svg class="badges" width="1200" height="444" viewBox="0 0 1200 444" role="img" aria-label="Partnerabzeichen: Ringpokal, Landesballverband, Kronenliga, Vesper Cup, Meridian Trophy">
    <circle cx="657" cy="222" r="40" fill="var(--badge)" stroke="var(--badge-edge)" stroke-width="3"/>
    <circle cx="750" cy="222" r="40" fill="var(--badge)" stroke="var(--badge-edge)" stroke-width="3"/>
    <rect x="840" y="174" width="86" height="86" rx="10" fill="var(--badge)" stroke="var(--badge-edge)" stroke-width="3"/>
    <circle cx="1015" cy="222" r="38" fill="var(--badge)" stroke="var(--badge-edge)" stroke-width="3"/>
    <circle cx="1111" cy="222" r="38" fill="var(--badge)" stroke="var(--badge-edge)" stroke-width="3"/>
  </svg>

  <div class="info-band">
    <p class="headline">Alle Sportevents live &amp; in HD</p>
    <p class="address">@ Kugelhaus, Fennweg 14, 72519 Reutlingen</p>
  </div>
</main>
</body>
</html>
```